Website Home Page for Women's Health Medical Office

Redesign existing homepage for website using existing logo. Current website location is www.lumawomenscare.com. Please give it a modern, streamlined, playful feel.

Please give it a feminine feel and make it bright and cheerful using logo colors.

Target Market(s)

Women between the ages of 25-45

Industry/Entity Type

Medical Office

Coding

Coded - Design and coding required

Number of Pages Required

1 page

Font styles to use
Sans Serif
Other font styles liked:
• SEGOI UI script for text and GIL SANS for bold (or their equivilent)

Colors
E54698
E96AAD
F1A4CE
F9D9EA
FCEFF6

Requirements
Must have
• Existing logo. Logo Colors. Feminine, cheerful, simple design. all relevant contact information
Nice to have
• clean lines and streamlined look
Should not have
• Cluttered

```html
<!DOCTYPE html>
<html lang="en">
<head>
<meta charset="utf-8">
<title>Luma Women's Care – Home</title>
<link rel="stylesheet" href="https://fonts.googleapis.com/css2?family=Poppins:wght@300;400;500;600;700&display=swap">
<style>
:root{
  --pink:#e54698;
  --pink-mid:#e96aad;
  --pink-soft:#f1a4ce;
  --pink-pale:#f9d9ea;
  --pink-mist:#fceff6;
  --ink:#3a3a3a;
  --grey:#8a8a8a;
  --white:#ffffff;
  --gold:#ffe07a;
}
*{box-sizing:border-box;margin:0;padding:0}
html,body{width:1200px;height:4696px;overflow:hidden;background:var(--white)}
body{font-family:"Poppins",sans-serif;color:var(--ink);position:relative}
.page{position:relative;width:1200px;height:4696px;overflow:hidden}
.abs{position:absolute}
.btn{display:inline-block;border:2px solid var(--pink);color:var(--pink);border-radius:6px;font-size:15px;font-weight:500;padding:8px 22px;background:var(--white)}
.eyebrow{color:var(--pink);font-size:18px;font-weight:600}
.h2{font-size:48px;font-weight:600;color:var(--pink);line-height:1.05;text-transform:uppercase}
.body-text{font-size:15px;line-height:1.55;color:#5a5a5a}

/* hero */
.hero{left:0;top:0;width:1200px;height:770px;background:linear-gradient(120deg,#f6c3de 0%,#e96aad 45%,#d9558f 100%)}
.hero-photo{left:0;top:0;width:1200px;height:770px;background:radial-gradient(circle at 75% 55%,rgba(255,240,248,.55),rgba(229,70,152,0) 45%),radial-gradient(circle at 20% 70%,rgba(255,220,235,.45),rgba(229,70,152,0) 40%)}
.topbar{left:0;top:0;width:1200px;height:40px;background:rgba(255,255,255,.92);font-size:12px;color:var(--pink);display:flex;gap:36px;justify-content:center;align-items:center;padding-left:260px}
.topbar span{display:flex;align-items:center;gap:6px}
.header{left:0;top:40px;width:1200px;height:100px;background:rgba(255,255,255,.85)}
.logo{left:130px;top:66px;display:flex;align-items:center;gap:14px}
.logo-dot{width:44px;height:44px;border-radius:50%;background:var(--pink)}
.logo-name{font-size:30px;font-weight:700;color:var(--pink)}
.nav{left:620px;top:78px;display:flex;gap:30px;font-size:14px;font-weight:600;color:var(--pink)}
.nav-cta{left:1000px;top:66px;border:2px solid var(--pink);border-radius:8px;padding:10px 18px;font-size:14px;font-weight:600;color:var(--pink)}
.welcome{left:0;top:288px;width:1200px;text-align:center;color:var(--white)}
.welcome .l1{font-size:66px;font-weight:700;letter-spacing:2px;line-height:1}
.welcome .l2{font-size:40px;font-weight:500;letter-spacing:1px;margin-top:6px}

/* feature cards */
.card{top:600px;width:220px;height:460px;background:var(--white);border-radius:14px;box-shadow:0 10px 30px rgba(229,70,152,.18);text-align:center;padding:34px 20px 0;border-bottom:6px solid var(--pink)}
.card-icon{width:70px;height:70px;margin:0 auto 16px}
.card h3{font-size:16px;font-weight:600;color:var(--pink);margin-bottom:12px}
.card p{font-size:12.5px;line-height:1.6;color:var(--grey);height:210px}
.card .btn{margin-top:16px}

/* serving */
.serving-text{left:130px;top:1265px;width:490px}
.serving-text .h2{margin:6px 0 26px}
.serving-text .body-text + .body-text{margin-top:22px}
.serving-text .btn{margin-top:28px}
.photo-round{border-radius:50%;background:linear-gradient(160deg,#f9d9ea,#c98aa8 60%,#7a4a5c)}
.photo-tag{width:124px;height:80px;border-radius:18px;background:var(--pink-mid);color:var(--white);font-size:24px;line-height:1;padding:16px 16px}
.photo-tag b{display:block;font-weight:600}

/* banner */
.banner{left:135px;top:1800px;width:930px;height:200px;border-radius:30px;background:linear-gradient(90deg,var(--pink) 0%,var(--pink-mid) 100%);box-shadow:0 10px 30px rgba(229,70,152,.3)}
.banner-text{left:220px;top:1862px;color:var(--white);display:flex;align-items:center;gap:16px}
.banner-text .t1{font-size:32px;font-weight:400;line-height:1}
.banner-text .t2{font-size:38px;font-weight:700;line-height:1.1}
.banner-cta{left:690px;top:1852px;width:300px;height:96px;border-radius:14px;background:rgba(255,255,255,.22);color:var(--white);font-size:17px;text-align:center;padding-top:18px;line-height:1.5}

/* specialists */
.spec-text{left:640px;top:2105px;width:440px}
.spec-text .h2{margin:6px 0 26px}
.spec-text .body-text{font-size:14px}
.spec-text .body-text + .body-text{margin-top:20px}

/* services */
.services{left:0;top:2830px;width:1200px;height:880px;background:linear-gradient(180deg,var(--pink-mid) 0%,var(--pink) 60%,var(--pink-mid) 100%)}
.services-head{left:0;top:2995px;width:1200px;text-align:center;color:var(--white)}
.services-head .s1{font-size:18px;font-weight:600;color:var(--gold)}
.services-head .s2{font-size:46px;font-weight:500}
.search{left:470px;top:3090px;width:260px;height:30px;background:var(--white);border-radius:4px}
.grid{left:120px;top:3180px;width:980px;display:grid;grid-template-columns:repeat(4,220px);column-gap:33px;row-gap:22px}
.pill{height:46px;border-radius:4px;background:var(--pink-soft);color:var(--white);display:flex;align-items:center;padding:0 12px;gap:12px;font-size:14px}
.pill.dark{background:#d33a88}
.pill .name{flex:1}

/* news */
.news-head{left:0;top:3755px;width:1200px;text-align:center}
.news-head .n2{font-size:46px;font-weight:500;color:var(--pink);letter-spacing:2px}
.news-card{top:3870px;width:290px}
.news-img{width:290px;height:170px;background:linear-gradient(135deg,#f9d9ea,#c8a3b6 55%,#8f6b7d)}
.news-card h3{font-size:26px;font-weight:600;color:var(--pink);margin:18px 0 8px}
.news-card p{font-size:12.5px;line-height:1.6;color:var(--grey)}
.news-card .btn{margin-top:20px}
.more{left:580px;top:4270px;width:42px;height:42px;border-radius:50%;background:var(--pink)}

/* newsletter */
.newsletter{left:0;top:4385px;width:1200px;height:95px;background:var(--pink)}
.nl-title{left:140px;top:4413px;color:var(--white);display:flex;align-items:center;gap:12px}
.nl-title b{font-size:24px;font-weight:700}
.nl-title span{font-size:24px;font-weight:300}
.nl-input{left:465px;top:4415px;width:320px;height:36px;background:var(--white);border-radius:4px;font-size:12px;color:#aaa;padding:10px 14px}
.nl-btn{left:830px;top:4415px;width:150px;height:36px;background:var(--pink-soft);border-radius:4px;font-size:12px;font-weight:600;color:var(--white);text-align:center;line-height:36px}

/* footer */
.foot-logo{left:140px;top:4510px;width:130px;text-align:center}
.foot-logo .logo-dot{width:40px;height:40px;margin:0 auto 6px}
.foot-logo .name{font-size:16px;font-weight:700;color:var(--pink)}
.foot-about{left:300px;top:4515px;width:200px;font-size:11px;line-height:1.55;color:var(--grey)}
.foot-nav{left:630px;top:4510px;font-size:12px;font-weight:600;color:var(--pink);line-height:1.55}
.foot-phones{left:930px;top:4512px;font-size:14px;font-weight:500;color:var(--pink);line-height:1.6}
.foot-phones div{display:flex;align-items:center;gap:8px}
.social{left:965px;top:4575px;display:flex;gap:14px}
.social span{width:22px;height:22px;border-radius:50%;background:var(--pink)}
.foot-bar{left:0;top:4640px;width:1200px;height:56px;background:var(--pink-mist);border-top:3px solid var(--pink);font-size:12px;color:var(--grey);display:flex;justify-content:space-between;align-items:center;padding:0 140px 0 520px}
.foot-bar .legal{color:var(--pink)}
</style>
</head>
<body>
<div class="page">

  <!-- hero -->
  <div class="abs hero" role="img" aria-label="Photo of a smiling mother holding her newborn, washed in pink"></div>
  <div class="abs hero-photo"></div>
  <div class="abs topbar">
    <span><svg width="12" height="12" viewBox="0 0 24 24"><path fill="#e54698" d="M6.6 10.8a15 15 0 006.6 6.6l2.2-2.2a1 1 0 011-.25 11.4 11.4 0 003.6.57 1 1 0 011 1V20a1 1 0 01-1 1A17 17 0 013 4a1 1 0 011-1h3.5a1 1 0 011 1c0 1.25.2 2.45.57 3.6a1 1 0 01-.25 1z"/></svg>(555) 014-2280 | (555) 014-2291</span>
    <span><svg width="13" height="10" viewBox="0 0 24 18"><rect x="1" y="1" width="22" height="16" rx="2" fill="none" stroke="#e54698" stroke-width="2"/><path d="M1 2l11 8 11-8" fill="none" stroke="#e54698" stroke-width="2"/></svg>hello@lumawomenscare.com</span>
    <span><svg width="10" height="13" viewBox="0 0 18 24"><path fill="#e54698" d="M9 0a9 9 0 00-9 9c0 7 9 15 9 15s9-8 9-15a9 9 0 00-9-9zm0 12a3 3 0 110-6 3 3 0 010 6z"/></svg>1180 Orchard Bloom Way, Suite 4, Cedar Vale, CA 90210</span>
  </div>
  <div class="abs header"></div>
  <div class="abs logo"><span class="logo-dot"></span><span class="logo-name">Luma Women's Care</span></div>
  <nav class="abs nav"><span>HOME</span><span>SERVICES</span><span>RESOURCES</span><span>ABOUT US</span></nav>
  <div class="abs nav-cta">CONTACT US</div>
  <div class="abs welcome">
    <div class="l1">WELCOME</div>
    <div class="l2">TO LUMA WOMEN'S CARE, CEDAR VALE, CA</div>
  </div>

  <!-- feature cards -->
  <div class="abs card" style="left:115px">
    <svg class="card-icon" viewBox="0 0 70 70"><circle cx="35" cy="35" r="33" fill="var(--pink-mist)"/><circle cx="35" cy="22" r="7" fill="none" stroke="#e54698" stroke-width="2.5"/><path d="M27 56V38a8 8 0 0116 0c4 2 6 6 4 11l-4 7" fill="none" stroke="#e54698" stroke-width="2.5" stroke-linecap="round"/></svg>
    <h3>PREGNANCY CARE</h3>
    <p>From your first visit to delivery day, our team guides you through every stage of pregnancy with warm, personal care, clear answers and checkups that fit your life and your growing family.</p>
    <span class="btn">Read More</span>
  </div>
  <div class="abs card" style="left:365px">
    <svg class="card-icon" viewBox="0 0 70 70"><circle cx="35" cy="35" r="33" fill="var(--pink-mist)"/><rect x="20" y="28" width="30" height="14" rx="7" fill="none" stroke="#e54698" stroke-width="2.5" transform="rotate(-35 35 35)"/><line x1="29" y1="43" x2="41" y2="27" stroke="#e54698" stroke-width="2.5"/></svg>
    <h3>BIRTH CONTROL</h3>
    <p>We help you compare every birth control option, from daily methods to long-acting choices, so you can pick the one that matches your health, your plans and your comfort with confidence.</p>
    <span class="btn">Read More</span>
  </div>
  <div class="abs card" style="left:615px">
    <svg class="card-icon" viewBox="0 0 70 70"><circle cx="35" cy="35" r="33" fill="var(--pink-mist)"/><path d="M18 40h34M22 40c0-8 6-14 13-14s13 6 13 14M30 46h10" fill="none" stroke="#e54698" stroke-width="2.5" stroke-linecap="round"/></svg>
    <h3>WELL WOMAN EXAMS</h3>
    <p>Yearly exams are the heart of staying well. We check in on your whole health, run the screenings you need and take time to listen to every question you bring to the visit.</p>
    <span class="btn">Read More</span>
  </div>
  <div class="abs card" style="left:865px">
    <svg class="card-icon" viewBox="0 0 70 70"><circle cx="35" cy="35" r="33" fill="var(--pink-mist)"/><path d="M35 52S17 41 17 29a9 9 0 0118-2 9 9 0 0118 2c0 12-18 23-18 23z" fill="none" stroke="#e54698" stroke-width="2.5"/><path d="M22 36h7l3-5 4 9 3-4h8" fill="none" stroke="#e54698" stroke-width="2"/></svg>
    <h3>WOMEN'S HEALTH</h3>
    <p>Whatever your stage of life, we treat the full range of women's health concerns with modern tools, gentle hands and a care plan built around you and your goals.</p>
    <span class="btn">Read More</span>
  </div>

  <!-- serving -->
  <div class="abs serving-text">
    <div class="eyebrow">Lorem Ipsum</div>
    <div class="h2">Serving Luma<br>Springs</div>
    <p class="body-text">At Luma Women's Care in Cedar Vale, California, we believe better health starts when the patient is educated. For this reason, we take time to listen to our patients' concerns, explain each option available, and answer any questions our patients may have so that they can make informed decisions. Our providers tailor every procedure and treatment option to meet the specific needs of each patient and keep up with the latest techniques and practice guidelines for women's health.</p>
    <p class="body-text">Our medical providers will take time to give you the personalized health care you deserve. This includes taking time to listen to you and screening you for problems to help ensure that any health issues are diagnosed and treated as early as possible.</p>
    <span class="btn">Talk To Us</span>
  </div>
  <div class="abs photo-round" style="left:630px;top:1200px;width:430px;height:430px" role="img" aria-label="Portrait of a smiling physician in a white coat"></div>
  <div class="abs photo-tag" style="left:680px;top:1555px"><b>Lorem</b>Ipsum</div>

  <!-- banner -->
  <div class="abs banner"></div>
  <div class="abs banner-text">
    <svg width="46" height="46" viewBox="0 0 46 46"><circle cx="23" cy="23" r="21" fill="none" stroke="#fff" stroke-width="2.5"/><path d="M14 23l6 6 12-12" fill="none" stroke="#fff" stroke-width="3" stroke-linecap="round"/></svg>
    <div><div class="t1">NOW ACCEPTING</div><div class="t2">NEW PATIENTS</div></div>
  </div>
  <div class="abs banner-cta">Click Here for an Appointment<br>or Call Us at <b>(555) 014-2280</b></div>

  <!-- specialists -->
  <div class="abs photo-round" style="left:140px;top:2140px;width:430px;height:430px;background:linear-gradient(160deg,#f9d9ea,#d7a3bb 55%,#8a5d72)" role="img" aria-label="Photo of a new mother holding her baby"></div>
  <div class="abs photo-tag" style="left:190px;top:2500px"><b>Lorem</b>Ipsum</div>
  <div class="abs spec-text">
    <div class="eyebrow">Lorem Ipsum</div>
    <div class="h2">Your OB/GYN<br>Specialists</div>
    <p class="body-text">Luma Women's Care offers you the best care possible in a personalized setting. We are currently accepting patients. Call our office now to make an appointment.</p>
    <p class="body-text">Luma Women's Care is located near Luma Springs Hospital in Cedar Vale, CA. It is a medical office that specializes in women-centered healthcare for women of all ages. Our team of exclusively female providers have years of experience taking care of women with a variety of pregnancy and gynecology concerns.</p>
    <p class="body-text">Whether you need a routine examination, help during your pregnancy, have questions on birth control, or another female concern, we offer the tools and expertise for our patients. That is why better health starts here.</p>
    <p class="body-text">Our office provides you with an environment where you can feel comfortable and where you know you will be in good hands. Our providers are devoted women's health specialists and board certified in obstetrics and gynecology, ready to care for you.</p>
  </div>

  <!-- services -->
  <div class="abs services"></div>
  <svg class="abs" style="left:0;top:2820px" width="1200" height="110" viewBox="0 0 1200 110"><path d="M0 10C200 70 400 90 600 60S1000 0 1200 30V0H0z" fill="#fff"/></svg>
  <div class="abs services-head"><div class="s1">Lorem Ipsum</div><div class="s2">Our services</div></div>
  <div class="abs search"><svg style="position:absolute;right:8px;top:6px" width="18" height="18" viewBox="0 0 24 24"><circle cx="10" cy="10" r="7" fill="none" stroke="#e54698" stroke-width="2.5"/><line x1="15" y1="15" x2="21" y2="21" stroke="#e54698" stroke-width="2.5"/></svg></div>
  <div class="abs grid">
    <div class="pill dark"><svg width="16" height="14" viewBox="0 0 16 14"><path d="M1 7l5 5 9-10" fill="none" stroke="#fff" stroke-width="2.5"/></svg><span class="name">Prenatal Visits</span><svg width="10" height="14" viewBox="0 0 10 14"><path d="M2 1l6 6-6 6" fill="none" stroke="#fff" stroke-width="2.5"/></svg></div>
    <div class="pill"><svg width="16" height="14" viewBox="0 0 16 14"><path d="M1 7l5 5 9-10" fill="none" stroke="#fff" stroke-width="2.5"/></svg><span class="name">Ultrasound</span><svg width="10" height="14" viewBox="0 0 10 14"><path d="M2 1l6 6-6 6" fill="none" stroke="#fff" stroke-width="2.5"/></svg></div>
    <div class="pill"><svg width="16" height="14" viewBox="0 0 16 14"><path d="M1 7l5 5 9-10" fill="none" stroke="#fff" stroke-width="2.5"/></svg><span class="name">Pap Smears</span><svg width="10" height="14" viewBox="0 0 10 14"><path d="M2 1l6 6-6 6" fill="none" stroke="#fff" stroke-width="2.5"/></svg></div>
    <div class="pill"><svg width="16" height="14" viewBox="0 0 16 14"><path d="M1 7l5 5 9-10" fill="none" stroke="#fff" stroke-width="2.5"/></svg><span class="name">Menopause</span><svg width="10" height="14" viewBox="0 0 10 14"><path d="M2 1l6 6-6 6" fill="none" stroke="#fff" stroke-width="2.5"/></svg></div>

    <div class="pill dark"><svg width="16" height="14" viewBox="0 0 16 14"><path d="M1 7l5 5 9-10" fill="none" stroke="#fff" stroke-width="2.5"/></svg><span class="name">High-Risk Care</span><svg width="10" height="14" viewBox="0 0 10 14"><path d="M2 1l6 6-6 6" fill="none" stroke="#fff" stroke-width="2.5"/></svg></div>
    <div class="pill"><svg width="16" height="14" viewBox="0 0 16 14"><path d="M1 7l5 5 9-10" fill="none" stroke="#fff" stroke-width="2.5"/></svg><span class="name">IUD Placement</span><svg width="10" height="14" viewBox="0 0 10 14"><path d="M2 1l6 6-6 6" fill="none" stroke="#fff" stroke-width="2.5"/></svg></div>
    <div class="pill"><svg width="16" height="14" viewBox="0 0 16 14"><path d="M1 7l5 5 9-10" fill="none" stroke="#fff" stroke-width="2.5"/></svg><span class="name">Breast Exams</span><svg width="10" height="14" viewBox="0 0 10 14"><path d="M2 1l6 6-6 6" fill="none" stroke="#fff" stroke-width="2.5"/></svg></div>
    <div class="pill"><svg width="16" height="14" viewBox="0 0 16 14"><path d="M1 7l5 5 9-10" fill="none" stroke="#fff" stroke-width="2.5"/></svg><span class="name">Fertility</span><svg width="10" height="14" viewBox="0 0 10 14"><path d="M2 1l6 6-6 6" fill="none" stroke="#fff" stroke-width="2.5"/></svg></div>

    <div class="pill dark"><svg width="16" height="14" viewBox="0 0 16 14"><path d="M1 7l5 5 9-10" fill="none" stroke="#fff" stroke-width="2.5"/></svg><span class="name">Delivery Care</span><svg width="10" height="14" viewBox="0 0 10 14"><path d="M2 1l6 6-6 6" fill="none" stroke="#fff" stroke-width="2.5"/></svg></div>
    <div class="pill"><svg width="16" height="14" viewBox="0 0 16 14"><path d="M1 7l5 5 9-10" fill="none" stroke="#fff" stroke-width="2.5"/></svg><span class="name">Contraception</span><svg width="10" height="14" viewBox="0 0 10 14"><path d="M2 1l6 6-6 6" fill="none" stroke="#fff" stroke-width="2.5"/></svg></div>
    <div class="pill"><svg width="16" height="14" viewBox="0 0 16 14"><path d="M1 7l5 5 9-10" fill="none" stroke="#fff" stroke-width="2.5"/></svg><span class="name">HPV Vaccine</span><svg width="10" height="14" viewBox="0 0 10 14"><path d="M2 1l6 6-6 6" fill="none" stroke="#fff" stroke-width="2.5"/></svg></div>
    <div class="pill"><svg width="16" height="14" viewBox="0 0 16 14"><path d="M1 7l5 5 9-10" fill="none" stroke="#fff" stroke-width="2.5"/></svg><span class="name">Pelvic Health</span><svg width="10" height="14" viewBox="0 0 10 14"><path d="M2 1l6 6-6 6" fill="none" stroke="#fff" stroke-width="2.5"/></svg></div>

    <div class="pill dark"><svg width="16" height="14" viewBox="0 0 16 14"><path d="M1 7l5 5 9-10" fill="none" stroke="#fff" stroke-width="2.5"/></svg><span class="name">Postpartum</span><svg width="10" height="14" viewBox="0 0 10 14"><path d="M2 1l6 6-6 6" fill="none" stroke="#fff" stroke-width="2.5"/></svg></div>
    <div class="pill"><svg width="16" height="14" viewBox="0 0 16 14"><path d="M1 7l5 5 9-10" fill="none" stroke="#fff" stroke-width="2.5"/></svg><span class="name">STI Testing</span><svg width="10" height="14" viewBox="0 0 10 14"><path d="M2 1l6 6-6 6" fill="none" stroke="#fff" stroke-width="2.5"/></svg></div>
    <div class="pill"><svg width="16" height="14" viewBox="0 0 16 14"><path d="M1 7l5 5 9-10" fill="none" stroke="#fff" stroke-width="2.5"/></svg><span class="name">Bone Density</span><svg width="10" height="14" viewBox="0 0 10 14"><path d="M2 1l6 6-6 6" fill="none" stroke="#fff" stroke-width="2.5"/></svg></div>
    <div class="pill"><svg width="16" height="14" viewBox="0 0 16 14"><path d="M1 7l5 5 9-10" fill="none" stroke="#fff" stroke-width="2.5"/></svg><span class="name">Hormone Care</span><svg width="10" height="14" viewBox="0 0 10 14"><path d="M2 1l6 6-6 6" fill="none" stroke="#fff" stroke-width="2.5"/></svg></div>

    <div class="pill dark"><svg width="16" height="14" viewBox="0 0 16 14"><path d="M1 7l5 5 9-10" fill="none" stroke="#fff" stroke-width="2.5"/></svg><span class="name">Lactation</span><svg width="10" height="14" viewBox="0 0 10 14"><path d="M2 1l6 6-6 6" fill="none" stroke="#fff" stroke-width="2.5"/></svg></div>
    <div class="pill"><svg width="16" height="14" viewBox="0 0 16 14"><path d="M1 7l5 5 9-10" fill="none" stroke="#fff" stroke-width="2.5"/></svg><span class="name">Colposcopy</span><svg width="10" height="14" viewBox="0 0 10 14"><path d="M2 1l6 6-6 6" fill="none" stroke="#fff" stroke-width="2.5"/></svg></div>
    <div class="pill"><svg width="16" height="14" viewBox="0 0 16 14"><path d="M1 7l5 5 9-10" fill="none" stroke="#fff" stroke-width="2.5"/></svg><span class="name">Minor Surgery</span><svg width="10" height="14" viewBox="0 0 10 14"><path d="M2 1l6 6-6 6" fill="none" stroke="#fff" stroke-width="2.5"/></svg></div>
    <div class="pill"><svg width="16" height="14" viewBox="0 0 16 14"><path d="M1 7l5 5 9-10" fill="none" stroke="#fff" stroke-width="2.5"/></svg><span class="name">Counseling</span><svg width="10" height="14" viewBox="0 0 10 14"><path d="M2 1l6 6-6 6" fill="none" stroke="#fff" stroke-width="2.5"/></svg></div>

    <div class="pill dark"><svg width="16" height="14" viewBox="0 0 16 14"><path d="M1 7l5 5 9-10" fill="none" stroke="#fff" stroke-width="2.5"/></svg><span class="name">Screenings</span><svg width="10" height="14" viewBox="0 0 10 14"><path d="M2 1l6 6-6 6" fill="none" stroke="#fff" stroke-width="2.5"/></svg></div>
    <div class="pill"><svg width="16" height="14" viewBox="0 0 16 14"><path d="M1 7l5 5 9-10" fill="none" stroke="#fff" stroke-width="2.5"/></svg><span class="name">Teen Visits</span><svg width="10" height="14" viewBox="0 0 10 14"><path d="M2 1l6 6-6 6" fill="none" stroke="#fff" stroke-width="2.5"/></svg></div>
    <div class="pill"><svg width="16" height="14" viewBox="0 0 16 14"><path d="M1 7l5 5 9-10" fill="none" stroke="#fff" stroke-width="2.5"/></svg><span class="name">Lab Tests</span><svg width="10" height="14" viewBox="0 0 10 14"><path d="M2 1l6 6-6 6" fill="none" stroke="#fff" stroke-width="2.5"/></svg></div>
    <div class="pill"><svg width="16" height="14" viewBox="0 0 16 14"><path d="M1 7l5 5 9-10" fill="none" stroke="#fff" stroke-width="2.5"/></svg><span class="name">Telehealth</span><svg width="10" height="14" viewBox="0 0 10 14"><path d="M2 1l6 6-6 6" fill="none" stroke="#fff" stroke-width="2.5"/></svg></div>
  </div>
  <svg class="abs" style="left:0;top:3620px" width="1200" height="100" viewBox="0 0 1200 100"><path d="M0 60C250 10 500 10 700 50S1050 100 1200 40V100H0z" fill="#fff"/></svg>

  <!-- news -->
  <div class="abs news-head"><div class="eyebrow">Lorem Ipsum</div><div class="n2">NEWS</div></div>
  <div class="abs news-card" style="left:130px">
    <div class="news-img" role="img" aria-label="Photo of a newborn baby resting"></div>
    <h3>Lorem Ipsum</h3>
    <p>A short update from our office on new services, seasonal health tips and changes to our visit hours, written for patients and their families.</p>
    <span class="btn">Read More</span>
  </div>
  <div class="abs news-card" style="left:455px">
    <div class="news-img" role="img" aria-label="Photo of a mother and newborn in a hospital bed"></div>
    <h3>Lorem Ipsum</h3>
    <p>A short update from our office on new services, seasonal health tips and changes to our visit hours, written for patients and their families.</p>
    <span class="btn">Read More</span>
  </div>
  <div class="abs news-card" style="left:780px">
    <div class="news-img" role="img" aria-label="Photo of a pregnant woman during an ultrasound scan"></div>
    <h3>Lorem Ipsum</h3>
    <p>A short update from our office on new services, seasonal health tips and changes to our visit hours, written for patients and their families.</p>
    <span class="btn">Read More</span>
  </div>
  <div class="abs more"><svg width="42" height="42" viewBox="0 0 42 42"><path d="M21 12v18M12 21h18" stroke="#fff" stroke-width="3" stroke-linecap="round"/></svg></div>

  <!-- newsletter -->
  <div class="abs newsletter"></div>
  <div class="abs nl-title">
    <svg width="34" height="26" viewBox="0 0 34 26"><rect x="1.5" y="1.5" width="31" height="23" rx="3" fill="none" stroke="#fff" stroke-width="2.5"/><path d="M2 3l15 11L32 3" fill="none" stroke="#fff" stroke-width="2.5"/></svg>
    <b>SIGNUP</b><span>NEWSLETTER</span>
  </div>
  <div class="abs nl-input">Enter Your Email Address</div>
  <div class="abs nl-btn">SIGN UP NOW</div>

  <!-- footer -->
  <div class="abs foot-logo"><div class="logo-dot"></div><div class="name">Luma Women's Care</div></div>
  <p class="abs foot-about">Caring for women at every stage of life with kind, modern medicine. Visit us in Cedar Vale or call today to book your next appointment.</p>
  <div class="abs foot-nav"><div>HOME</div><div>SERVICES</div><div>RESOURCES</div><div>ABOUT US</div><div>CONTACT US</div></div>
  <div class="abs foot-phones">
    <div><svg width="12" height="12" viewBox="0 0 24 24"><path fill="#e54698" d="M6.6 10.8a15 15 0 006.6 6.6l2.2-2.2a1 1 0 011-.25 11.4 11.4 0 003.6.57 1 1 0 011 1V20a1 1 0 01-1 1A17 17 0 013 4a1 1 0 011-1h3.5a1 1 0 011 1c0 1.25.2 2.45.57 3.6a1 1 0 01-.25 1z"/></svg>(555) 014-2280</div>
    <div><svg width="12" height="12" viewBox="0 0 24 24"><path fill="#e54698" d="M6.6 10.8a15 15 0 006.6 6.6l2.2-2.2a1 1 0 011-.25 11.4 11.4 0 003.6.57 1 1 0 011 1V20a1 1 0 01-1 1A17 17 0 013 4a1 1 0 011-1h3.5a1 1 0 011 1c0 1.25.2 2.45.57 3.6a1 1 0 01-.25 1z"/></svg>(555) 014-2291</div>
  </div>
  <div class="abs social"><span></span><span></span></div>
  <div class="abs foot-bar"><span>© 2024 Luma Women's Care. All rights reserved.</span><span class="legal">Terms of Use | Privacy Statement</span></div>

</div>
</body>
</html>
```